New Business Card Design Project

Hi! I would like for you to design a business card for our aesthetic injections business. We offer Zelvia, filler, skin care. I would like it to be elegant, feminine, modern and sleek/clean. I like black/gold foil/ivory/parchment colors. It can be either one or two sided. I would like matte black with gold foil logo on one side and ivory with gold foil information on the other side

Target Market(s)

target market is the discerning woman who wants to look her best

Industry/Entity Type

beauty

Contact Information for Business Card

logo, name, phone, email, website, instagram, facebook, location

Requirements
Must have
• logo and info
Nice to have
• the icons for cell, instagram, email, fb etc
Should not have
• images of people

```html
<!DOCTYPE html>
<html lang="en">
<head>
<meta charset="utf-8">
<title>The Velmore Lounge – Business Card</title>
<link rel="stylesheet" href="https://fonts.googleapis.com/css2?family=Libre+Baskerville:wght@400;700&family=Montserrat:wght@600&family=Teko:wght@500&display=swap">
<style>
  :root {
    --page: #f4f4f2;
    --matte: #161616;
    --matte-soft: #222120;
    --ivory: #f7f1e3;
    --parchment: #ede2c8;
    --foil-light: #e8c574;
    --foil: #c99a45;
    --foil-deep: #9c7029;
  }
  * { box-sizing: border-box; margin: 0; padding: 0; }
  html, body {
    width: 1200px; height: 1200px; overflow: hidden;
    background: var(--page);
  }
  .canvas { position: relative; width: 1200px; height: 1200px; }

  .card {
    position: absolute; left: 205px; width: 793px; height: 452px;
    border-radius: 40px; overflow: hidden;
  }

  /* Logo side: matte black with gold foil */
  .card--front {
    top: 103px;
    background: linear-gradient(90deg, var(--matte) 0%, var(--matte-soft) 55%, var(--matte) 100%);
  }
  .front-frame {
    position: absolute; left: 38px; top: 37px; width: 680px; height: 377px;
    border: 2px solid var(--foil); border-right: none;
    border-radius: 14px 0 0 14px;
  }
  .brand-mark {
    position: absolute; left: 210px; top: 94px; width: 126px; height: 126px;
    border: 1.5px solid var(--foil); border-radius: 50%;
    display: flex; align-items: center; justify-content: center;
  }
  .brand-mark__name {
    font-family: "Libre Baskerville", serif; font-weight: 700;
    font-size: 17px; letter-spacing: 2px; color: var(--foil-light);
  }
  .brand-title {
    position: absolute; left: 96px; top: 258px;
    font-family: "Libre Baskerville", serif; font-weight: 700;
    font-size: 25px; letter-spacing: 2px; color: var(--foil-light);
  }
  .ornament--front {
    position: absolute; right: 0; top: 8px; width: 225px; height: 436px;
    background: radial-gradient(ellipse at 70% 50%, rgba(201,154,69,0.5) 0%, rgba(201,154,69,0.25) 45%, rgba(201,154,69,0) 72%);
  }

  /* Info side: ivory with gold foil */
  .card--back {
    top: 645px;
    background: linear-gradient(90deg, var(--parchment) 0%, var(--ivory) 40%, var(--ivory) 100%);
  }
  .back-frame {
    position: absolute; left: 83px; top: 40px; width: 672px; height: 377px;
    border: 1.5px solid var(--foil); border-radius: 14px;
  }
  .ornament--back {
    position: absolute; left: 0; top: 5px; width: 225px; height: 442px;
    background: radial-gradient(ellipse at 25% 50%, rgba(201,154,69,0.55) 0%, rgba(201,154,69,0.28) 45%, rgba(201,154,69,0) 72%);
  }
  .person {
    position: absolute; right: 83px; top: 54px; text-align: right;
  }
  .person__name {
    font-family: "Teko", sans-serif; font-weight: 500;
    font-size: 58px; line-height: 58px; letter-spacing: 2px;
    background: linear-gradient(90deg, var(--foil), var(--foil-deep));
    -webkit-background-clip: text; background-clip: text; color: transparent;
  }
  .person__role {
    font-family: "Montserrat", sans-serif; font-weight: 600;
    font-size: 20px; letter-spacing: 1px; color: var(--foil-deep); margin-top: 0;
  }
  .person__rule {
    width: 152px; height: 2px; background: var(--foil); margin: 14px 0 0 auto;
  }
  .contacts { position: absolute; right: 85px; top: 160px; list-style: none; }
  .contact {
    display: flex; align-items: center; justify-content: flex-end;
    height: 39.5px;
    font-family: "Libre Baskerville", serif; font-size: 13px; letter-spacing: 0.5px;
    color: var(--foil-deep);
  }
  .contact__icon { width: 18px; height: 18px; margin-left: 22px; flex: none; }
  .contact__icon svg { width: 18px; height: 18px; display: block; }
</style>
</head>
<body>
<main class="canvas">

  <section class="card card--front" aria-label="Card front">
    <div class="front-frame"></div>
    <div class="brand-mark"><span class="brand-mark__name">VELMORE</span></div>
    <h1 class="brand-title">THE VELMORE LOUNGE</h1>
    <div class="ornament--front" role="img" aria-label="Gold foil filigree scroll ornament on the right edge"></div>
  </section>

  <section class="card card--back" aria-label="Card back">
    <div class="back-frame"></div>
    <div class="ornament--back" role="img" aria-label="Gold foil filigree scroll ornament on the left edge"></div>

    <div class="person">
      <h2 class="person__name">YOUR NAME</h2>
      <p class="person__role">Graphic Designer</p>
      <div class="person__rule"></div>
    </div>

    <ul class="contacts">
      <li class="contact">123 Dummy, Lorem Ipsum
        <span class="contact__icon"><svg viewBox="0 0 24 24"><path fill="var(--foil-deep)" d="M12 2a7 7 0 0 0-7 7c0 5 7 13 7 13s7-8 7-13a7 7 0 0 0-7-7zm0 9.5a2.5 2.5 0 1 1 0-5 2.5 2.5 0 0 1 0 5z"/></svg></span></li>
      <li class="contact">+00 1234 5678 9012
        <span class="contact__icon"><svg viewBox="0 0 24 24"><path fill="var(--foil-deep)" d="M6.6 10.8a15 15 0 0 0 6.6 6.6l2.2-2.2a1 1 0 0 1 1-.25 11.4 11.4 0 0 0 3.6.57 1 1 0 0 1 1 1V20a1 1 0 0 1-1 1A17 17 0 0 1 3 4a1 1 0 0 1 1-1h3.5a1 1 0 0 1 1 1c0 1.25.2 2.45.57 3.6a1 1 0 0 1-.25 1z"/></svg></span></li>
      <li class="contact">hello@velmorelounge.com
        <span class="contact__icon"><svg viewBox="0 0 24 24"><rect x="2" y="5" width="20" height="14" rx="1.5" fill="none" stroke="var(--foil-deep)" stroke-width="2"/><path d="M2.5 6l9.5 7 9.5-7" fill="none" stroke="var(--foil-deep)" stroke-width="2"/></svg></span></li>
      <li class="contact">thevelmorelounge.com
        <span class="contact__icon"><svg viewBox="0 0 24 24"><path fill="var(--foil-deep)" d="M5 2l14 11-6.5.6 3.8 7.4-2.6 1.3-3.8-7.5L5 19.5z"/></svg></span></li>
      <li class="contact">@velmorelounge
        <span class="contact__icon"><svg viewBox="0 0 24 24"><circle cx="12" cy="12" r="7" fill="none" stroke="var(--foil-deep)" stroke-width="2"/></svg></span></li>
      <li class="contact">@velmorelounge
        <span class="contact__icon"><svg viewBox="0 0 24 24"><rect x="4" y="4" width="16" height="16" rx="3" fill="none" stroke="var(--foil-deep)" stroke-width="2"/></svg></span></li>
    </ul>
  </section>

</main>
</body>
</html>
```